Accountability Project Graphics

I want to create 10 social media graphics (new Instagram size 4:5 (1080 x 1350 pixels) focusing on our Quenral Accountability App, using any of the 3 pictures attached. Use the attached pics only, NO RANDOM STOCK PHOTOGRAPHY. For the color scheme, use the landing page colors/fonts (attached).
You can add any of the 3 photos attached but I mainly need BOLD text that includes these headlines and sub-headlines on them.
Please NOTE for all the headlines below, also add this sub-headline on each graphic:
Stay Consistent with RB in Your Pocket!
Here are the headlines:
• Stop Starting Over Every Monday
• You don't need more willpower. You need more support
• Built for women who are tired of doing this alone
• When Motivation Fades, RB Checks In
• The Support System You've Been Missing
• Support When Motivation Disappears
• What if RB Checked in Every Day?
• The Missing Piece Isn't Another Diet
• Eat the food you love. Stay accountable every day.
• One Bad Meal Doesn't Mean You Failed
Target Market(s)
women over 40 trying to lose weight
Look and feel
Each slider illustrates characteristics of the customer's brand and the style your logo design should communicate.

```html
<!DOCTYPE html>
<html lang="en">
<head>
<meta charset="utf-8">
<title>Quenral Accountability App – Social Graphics</title>
<link href="https://fonts.googleapis.com/css2?family=DM+Serif+Display&family=Caveat+Brush&family=Poppins:wght@400;500;600;700;800&display=swap" rel="stylesheet">
<style>
:root{
  --ink:#1d0f3a;
  --pink:#e8175d;
  --blush:#fde8f1;
  --blush-deep:#f6cfe0;
  --band:#2b0f4c;
  --white:#ffffff;
  --photo-a:#3a2a44;
  --photo-b:#c7a0b4;
  --pair-a:#9a6a86;
  --pair-b:#e3bfd0;
  --serif:'DM Serif Display', Georgia, serif;
  --script:'Caveat Brush', cursive;
  --sans:'Poppins', Arial, sans-serif;
}
*{box-sizing:border-box;margin:0;padding:0}
html,body{width:1200px;height:1181px;overflow:hidden;background:#fff}
.canvas{position:relative;width:1200px;height:1181px;font-family:var(--sans);color:var(--ink)}
.panel{position:absolute;overflow:hidden;background:linear-gradient(160deg,var(--blush) 0%,#fbdbe9 60%,var(--blush-deep) 100%)}
.panel > *{z-index:2}
.panel > .photo{z-index:0}
.photo{position:absolute;border-radius:40% 40% 8px 8px;background:linear-gradient(180deg,var(--photo-b) 0%,var(--photo-a) 70%)}
.photo.pair{border-radius:30px 30px 6px 6px;background:linear-gradient(180deg,var(--pair-b) 0%,var(--pair-a) 100%)}
.head{position:absolute;font-family:var(--serif);line-height:.95;color:var(--ink)}
.head .pink{color:var(--pink)}
.script{font-family:var(--script);color:var(--pink);line-height:1;white-space:nowrap}
.underline{display:block;height:3px;background:var(--pink);border-radius:3px;margin-top:3px}
.list{position:absolute;list-style:none;font-size:10px;font-weight:600;line-height:1.2}
.list li{display:flex;align-items:center;gap:7px;white-space:nowrap}
.tick{flex:none;width:14px;height:14px;border-radius:50%;background:var(--pink);position:relative}
.tick::after{content:"";position:absolute;left:4.5px;top:3px;width:3px;height:6px;border:solid #fff;border-width:0 2px 2px 0;transform:rotate(45deg)}
.band{position:absolute;display:flex;align-items:center;gap:8px;background:var(--band);color:var(--white);border-radius:12px;font-weight:600;font-size:12px;padding:0 12px;white-space:nowrap}
.band em{font-style:normal;color:var(--pink)}
.heart{flex:none}
.pill{background:rgba(255,255,255,.88);border-radius:12px;display:flex;align-items:center;gap:8px;padding:4px 8px;white-space:nowrap}
.ico{flex:none;width:22px;height:22px;border-radius:50%;background:var(--pink);display:flex;align-items:center;justify-content:center;color:#fff;font-size:10px;font-weight:700}
.badge{width:22px;height:22px;border-radius:50%;background:var(--pink);color:#fff;font-weight:700;font-size:11px;display:flex;align-items:center;justify-content:center}
</style>
</head>
<body>
<main class="canvas">

<!-- 1 Stop Starting Over -->
<section class="panel" style="left:0;top:0;width:352px;height:431px">
  <div class="photo" role="img" aria-label="Smiling woman in black lace top, hand on hip" style="left:205px;top:12px;width:145px;height:390px"></div>
  <h2 class="head" style="left:32px;top:50px;font-size:46px">Stop<br><span class="pink" style="font-size:40px">Starting<br>Over</span></h2>
  <p class="script" style="position:absolute;left:32px;top:172px;font-size:32px;color:var(--ink)">Every Monday</p>
  <p style="position:absolute;left:32px;top:224px;font-size:12.5px;font-weight:600;line-height:1.35">Stay Consistent with<br><span style="color:var(--pink)">RB in Your Pocket!</span></p>
  <div style="position:absolute;left:24px;top:268px;width:162px;display:flex;flex-direction:column;gap:5px;font-size:9px;line-height:1.2">
    <div class="pill"><span class="ico">✆</span><span><b>Daily check-ins</b><br>that keep you on track</span></div>
    <div class="pill"><span class="ico">♥</span><span><b>Real support</b><br>that keeps you going</span></div>
    <div class="pill"><span class="ico">✓</span><span><b>Accountability</b><br>that gets results</span></div>
  </div>
  <div class="pill" style="position:absolute;left:205px;top:323px;width:115px;height:56px;font-size:9.5px;font-weight:500;justify-content:center;text-align:center">You got this!<br>I'm here for you.</div>
  <div class="badge" style="position:absolute;left:196px;top:312px">RB</div>
  <div class="band" style="left:10px;top:389px;width:324px;height:40px;font-size:12.5px">
    <svg class="heart" width="20" height="18" viewBox="0 0 24 22"><path d="M12 20S2 13 2 7a5 5 0 0 1 10-1 5 5 0 0 1 10 1c0 6-10 13-10 13z" fill="none" stroke="#e8175d" stroke-width="2"/></svg>
    <span>Stay Consistent with <em>RB in Your Pocket!</em></span>
  </div>
</section>

<!-- 2 Willpower -->
<section class="panel" style="left:358px;top:0;width:258px;height:431px">
  <h2 class="head" style="left:20px;top:52px;font-size:29px">You don't<br>need more</h2>
  <p style="position:absolute;left:20px;top:108px;font-weight:800;font-size:32px;color:var(--pink);letter-spacing:-.5px;white-space:nowrap">WILLPOWER.</p>
  <p class="head" style="left:20px;top:152px;font-size:22px">You need more</p>
  <p class="script" style="position:absolute;left:22px;top:172px;font-size:34px">SUPPORT. ♡<span class="underline" style="width:110px;margin-left:50px"></span></p>
  <div class="photo pair" role="img" aria-label="Two laughing women in denim jackets" style="left:10px;top:215px;width:240px;height:135px"></div>
  <div style="position:absolute;left:8px;top:335px;width:244px;display:flex;justify-content:space-between;text-align:center;font-size:8.5px;font-weight:600;line-height:1.2">
    <div><div class="ico" style="width:48px;height:48px;background:#fff;color:var(--pink);font-size:20px;margin:0 auto 4px">●●</div>Real<br>people.</div>
    <div><div class="ico" style="width:48px;height:48px;background:#fff;color:var(--pink);font-size:20px;margin:0 auto 4px">▣</div>Real<br>accountability.</div>
    <div><div class="ico" style="width:48px;height:48px;background:#fff;color:var(--pink);font-size:22px;margin:0 auto 4px">♥</div>Real<br>support.</div>
    <div><div class="ico" style="width:48px;height:48px;background:#fff;color:var(--pink);font-size:20px;margin:0 auto 4px">🏆︎</div>Real<br>results.</div>
  </div>
  <span class="underline" style="position:absolute;left:40px;top:408px;width:180px"></span>
</section>

<!-- 3 Built for women -->
<section class="panel" style="left:622px;top:0;width:295px;height:431px">
  <div class="photo" role="img" aria-label="Laughing woman with curly hair in denim dress" style="left:175px;top:62px;width:118px;height:320px"></div>
  <h2 class="head" style="left:24px;top:52px;font-size:27px">Built for<br>women who<br>are tired of<br>doing this</h2>
  <p class="script" style="position:absolute;left:24px;top:158px;font-size:44px">ALONE. ♡<span class="underline" style="width:150px"></span></p>
  <ul class="list" style="left:20px;top:236px;display:flex;flex-direction:column;gap:9px;font-size:9.5px;font-weight:500">
    <li><span class="tick"></span>Daily check-ins from RB</li>
    <li><span class="tick"></span>Encouragement that<br>keeps you going</li>
    <li><span class="tick"></span>Support that holds<br>you accountable</li>
    <li><span class="tick"></span>A community that<br>gets it</li>
  </ul>
  <div style="position:absolute;left:18px;top:360px;width:272px;height:68px;background:var(--pink);border-radius:8px 30px 8px 30px;transform:skewX(-6deg);color:#fff;text-align:center;font-weight:600;font-size:13.5px;line-height:1.35;padding-top:12px;white-space:nowrap">Stay Consistent with<br><span style="font-size:15px">RB in Your Pocket!</span></div>
</section>

<!-- 4 When Motivation Fades -->
<section class="panel" style="left:923px;top:0;width:277px;height:431px">
  <div class="photo" role="img" aria-label="Smiling woman looking at her phone" style="left:172px;top:40px;width:105px;height:360px"></div>
  <h2 class="head" style="left:20px;top:58px;font-size:28px">When<br>Motivation<br>Fades,</h2>
  <p class="script" style="position:absolute;left:20px;top:146px;font-size:29px">RB Checks In<span class="underline" style="width:130px"></span></p>
  <div style="position:absolute;left:11px;top:218px;width:142px;display:flex;flex-direction:column;gap:6px;font-size:8px;font-weight:500">
    <div class="pill"><span class="ico">…</span>RB: You good, sis? <span style="color:var(--pink)">♥</span></div>
    <div class="pill"><span class="ico">☺</span>How was your day?</div>
    <div class="pill"><span class="ico">●</span>Need some<br>encouragement?</div>
    <div class="pill"><span class="ico">●</span>I'm here for you!</div>
  </div>
  <div class="band" style="left:10px;top:378px;width:242px;height:50px;font-size:12px;line-height:1.3">
    <svg class="heart" width="26" height="24" viewBox="0 0 24 22"><path d="M12 20S2 13 2 7a5 5 0 0 1 10-1 5 5 0 0 1 10 1c0 6-10 13-10 13z" fill="none" stroke="#e8175d" stroke-width="2"/></svg>
    <span>Stay Consistent with<br><em>RB in Your Pocket!</em></span>
  </div>
</section>

<!-- 5 Support System -->
<section class="panel" style="left:0;top:440px;width:310px;height:343px">
  <div class="photo pair" role="img" aria-label="Two women embracing and laughing" style="left:170px;top:58px;width:140px;height:250px"></div>
  <h2 class="head" style="left:22px;top:48px;font-size:26px">The Support<br>System</h2>
  <p class="script" style="position:absolute;left:22px;top:102px;font-size:30px;line-height:1.05">You've Been<br>Missing ♡<span class="underline" style="width:128px"></span></p>
  <ul class="list" style="left:22px;top:190px;display:flex;flex-direction:column;gap:7px;font-size:9.5px">
    <li><span class="tick"></span>Daily check-ins</li>
    <li><span class="tick"></span>Encouragement</li>
    <li><span class="tick"></span>Accountability</li>
    <li><span class="tick"></span>Text support</li>
    <li><span class="tick"></span>Meal help &amp; ideas</li>
  </ul>
  <div class="band" style="left:10px;top:307px;width:292px;height:34px;font-size:11.5px;padding:0 10px">
    <span class="ico" style="width:18px;height:18px;font-size:10px">♥</span>
    <span>Stay Consistent with <em>RB in Your Pocket!</em></span>
  </div>
</section>

<!-- 6 Support When Motivation Disappears -->
<section class="panel" style="left:316px;top:440px;width:300px;height:343px">
  <div style="position:absolute;left:180px;top:118px;width:108px;height:205px;border-radius:18px;background:var(--band);transform:rotate(6deg);border:4px solid #1a1a1a;color:#fff;text-align:center;font-size:10px;font-style:italic;line-height:1.8;z-index:1">
    <div class="badge" style="width:30px;height:30px;margin:26px auto 12px;font-style:normal">RB</div>
    Checking in...<br>How are you<br>doing today?
    <div style="margin:12px auto 0;width:70px;height:26px;border-radius:8px;background:var(--pink);font-weight:700;font-size:12px;line-height:26px">I'M IN!</div>
  </div>
  <div class="ico" style="position:absolute;left:264px;top:106px;width:24px;height:24px">●</div>
  <h2 class="head" style="left:16px;top:46px;font-size:26px">Support When<br>Motivation</h2>
  <p class="script" style="position:absolute;left:18px;top:102px;font-size:30px">DISAPPEARS<span class="underline" style="width:150px"></span></p>
  <ul class="list" style="left:16px;top:163px;display:flex;flex-direction:column;gap:10px;font-size:9.5px;font-weight:500">
    <li><span class="tick"></span>RB checks in daily</li>
    <li><span class="tick"></span>Keeps you accountable</li>
    <li><span class="tick"></span>Encourages you</li>
    <li><span class="tick"></span>Helps you reset</li>
    <li><span class="tick"></span>Keeps you moving<br>forward</li>
  </ul>
  <div style="position:absolute;left:0;top:308px;width:262px;height:34px;background:#fff;border-radius:0 12px 0 0;color:var(--pink);font-weight:600;font-size:11px;line-height:34px;padding-left:15px;white-space:nowrap">Stay Consistent with RB in Your Pocket!</div>
</section>

<!-- 7 What if RB -->
<section class="panel" style="left:622px;top:440px;width:288px;height:343px">
  <div class="photo" role="img" aria-label="Smiling woman with arms crossed" style="left:165px;top:25px;width:123px;height:290px"></div>
  <h2 class="head" style="left:12px;top:50px;font-size:25px">&nbsp;What if<br>RB Checked in</h2>
  <p class="script" style="position:absolute;left:12px;top:100px;font-size:30px">EVERY DAY?<span class="underline" style="width:128px"></span></p>
  <ul class="list" style="left:12px;top:165px;display:flex;flex-direction:column;gap:9px;font-size:10px;font-weight:500">
    <li><span class="tick"></span>Daily accountability</li>
    <li><span class="tick"></span>Real support</li>
    <li><span class="tick"></span>Meal help &amp; ideas</li>
    <li><span class="tick"></span>Encouragement</li>
    <li><span class="tick"></span>Results that last</li>
  </ul>
  <div class="band" style="left:6px;top:305px;width:234px;height:38px;font-size:9.5px;border-radius:10px 10px 0 0;padding:0 10px">
    <span>Stay Consistent with <em>RB in Your Pocket!</em></span>
  </div>
  <svg style="position:absolute;left:240px;top:298px" width="34" height="32" viewBox="0 0 24 22"><path d="M12 20S2 13 2 7a5 5 0 0 1 10-1 5 5 0 0 1 10 1c0 6-10 13-10 13z" fill="none" stroke="#e8175d" stroke-width="2"/></svg>
</section>

<!-- 8 Missing Piece -->
<section class="panel" style="left:917px;top:440px;width:283px;height:343px">
  <div class="photo pair" role="img" aria-label="Two laughing women in denim" style="left:168px;top:150px;width:115px;height:160px"></div>
  <h2 class="head" style="left:16px;top:50px;font-size:25px">The Missing<br>Piece Isn't<br>Another <span class="script" style="font-size:28px">DIET</span></h2>
  <span class="underline" style="position:absolute;left:16px;top:140px;width:160px"></span>
  <ul class="list" style="left:14px;top:180px;display:flex;flex-direction:column;gap:14px;font-size:9.5px;font-weight:500">
    <li><span class="tick" style="border-radius:3px"></span>It's Accountability</li>
    <li><span class="tick" style="border-radius:3px"></span>It's Daily Support</li>
    <li><span class="tick" style="border-radius:3px"></span>It's Consistency</li>
    <li><span class="tick" style="border-radius:3px"></span>It's RB in Your Pocket!</li>
  </ul>
  <div class="band" style="left:10px;top:305px;width:263px;height:38px;font-size:10.5px;border-radius:10px 10px 0 0;padding:0 10px">
    <span>Stay Consistent with <em>RB in Your Pocket!</em></span>
  </div>
</section>

<!-- 9 Eat the food you love -->
<section class="panel" style="left:0;top:792px;width:606px;height:389px">
  <div class="photo" role="img" aria-label="Smiling woman in black lace top, hand on hip" style="left:270px;top:0;width:130px;height:350px"></div>
  <h2 class="head" style="left:32px;top:44px;font-size:42px;line-height:.98">Eat the<br><span style="font-size:36px">food you love.</span></h2>
  <p class="head" style="left:32px;top:132px;font-size:30px;color:var(--pink);line-height:1.05">Stay accountable<br>every day. <span class="script">♡</span></p>
  <span class="underline" style="position:absolute;left:32px;top:208px;width:160px"></span>
  <div role="img" aria-label="Bowl of fresh berries" style="position:absolute;left:0;top:228px;width:130px;height:95px;border-radius:50%;background:radial-gradient(#d94a5a,#e9e3ea 70%)"></div>
  <div role="img" aria-label="Plate with a burger" style="position:absolute;left:125px;top:218px;width:195px;height:115px;border-radius:50%;background:radial-gradient(#c07a36,#f3e7ef 70%)"></div>
  <div role="img" aria-label="Plate with a chocolate dessert" style="position:absolute;left:410px;top:250px;width:185px;height:100px;border-radius:50%;background:radial-gradient(#5b3424,#f5dde8 70%)"></div>
  <div style="position:absolute;left:405px;top:32px;width:180px;display:flex;flex-direction:column;gap:8px;font-size:12px;font-weight:500;line-height:1.3">
    <div class="pill" style="padding:10px 12px;gap:12px"><span class="ico" style="width:34px;height:34px;font-size:16px">✓</span>Enjoy the foods<br>you love</div>
    <div class="pill" style="padding:10px 12px;gap:12px"><span class="ico" style="width:34px;height:34px;font-size:14px">✕</span>Get meal help &amp;<br>ideas daily</div>
    <div class="pill" style="padding:10px 12px;gap:12px"><span class="ico" style="width:34px;height:34px;font-size:18px">♥</span>Stay accountable<br>with RB</div>
  </div>
  <div class="band" style="left:0;top:320px;width:440px;height:52px;font-size:16px;border-radius:0 12px 12px 0;padding-left:16px">
    <svg class="heart" width="30" height="28" viewBox="0 0 24 22"><path d="M12 20S2 13 2 7a5 5 0 0 1 10-1 5 5 0 0 1 10 1c0 6-10 13-10 13z" fill="none" stroke="#e8175d" stroke-width="2"/></svg>
    <span>Stay Consistent with <em>RB in Your Pocket!</em></span>
  </div>
</section>

<!-- 10 One Bad Meal -->
<section class="panel" style="left:614px;top:792px;width:586px;height:389px">
  <div class="photo pair" role="img" aria-label="Two women embracing and laughing" style="left:340px;top:10px;width:246px;height:379px"></div>
  <h2 class="head" style="left:26px;top:48px;font-size:44px">One Bad Meal<br>Doesn't Mean</h2>
  <p class="script" style="position:absolute;left:28px;top:140px;font-size:50px">You Failed. ♡</p>
  <span class="underline" style="position:absolute;left:30px;top:198px;width:210px"></span>
  <div style="position:absolute;left:22px;top:222px;width:458px;height:104px;background:rgba(255,255,255,.92);border-radius:16px;display:flex;align-items:center;text-align:center;font-size:12.5px;font-weight:500;line-height:1.3">
    <div style="flex:1"><div style="color:var(--pink);font-size:30px;line-height:1">⟳</div>Reset,<br>Don't Quit</div>
    <div style="flex:1;border-left:1px solid #eed3df"><div class="badge" style="width:36px;height:36px;margin:0 auto 4px;font-size:14px">RB</div>RB is Here<br>for You</div>
    <div style="flex:1.1;border-left:1px solid #eed3df"><div style="color:var(--pink);font-size:28px;line-height:1.1">▣</div>Stay Consistent<br>Tomorrow</div>
    <div style="flex:1.1;border-left:1px solid #eed3df"><div style="color:var(--pink);font-size:26px;line-height:1.15">🏆︎</div>Progress<br>Over Perfection</div>
  </div>
  <p style="position:absolute;left:80px;top:344px;font-family:var(--serif);font-size:19px;white-space:nowrap">Stay Consistent with <span style="color:var(--pink)">RB in Your Pocket</span>!</p>
  <svg style="position:absolute;left:500px;top:318px" width="54" height="50" viewBox="0 0 24 22"><path d="M12 20S2 13 2 7a5 5 0 0 1 10-1 5 5 0 0 1 10 1c0 6-10 13-10 13z" fill="none" stroke="#e8175d" stroke-width="1.6"/></svg>
</section>

</main>
</body>
</html>
```